Quiet Fern Acupuncture
Quiet Fern Acupuncture -
Creative Brief
Bright & Fun-filled
Marla Pennick-Vasquez
LAc, Dipl, Ac
2730 N Ridley Avenue, Suite 410 Flagstaff, AZ, 86044 @ Haverstock Chiropractic
quietfernacupuncture@mailbox-example.com
an appointment reminder card

```html
<!DOCTYPE html>
<html lang="en">
<head>
<meta charset="utf-8">
<title>Quiet Fern Acupuncture – Appointment Card</title>
<link rel="stylesheet" href="https://fonts.googleapis.com/css2?family=Source+Sans+3:wght@400;600&display=swap">
<style>
  :root {
    --backdrop: #ece8e2;
    --card-white: #ffffff;
    --orange-deep: #f06a12;
    --orange-light: #fbb040;
    --edge-black: #111111;
    --ink: #2b2b2b;
    --ink-soft: #3a3a3a;
    --accent: #f26b1d;
    --brand-circle: #f7941d;
  }
  html, body {
    margin: 0;
    padding: 0;
    width: 1200px;
    height: 778px;
    overflow: hidden;
    background: var(--backdrop);
    font-family: "Source Sans 3", "Helvetica Neue", Arial, sans-serif;
  }
  .canvas {
    position: relative;
    width: 1200px;
    height: 778px;
  }
  .card {
    position: absolute;
    left: 160px;
    top: 139px;
    width: 880px;
    height: 500px;
    border-radius: 36px;
    overflow: hidden;
    box-shadow: 0 6px 18px rgba(0,0,0,0.18);
  }
  .card-shape {
    position: absolute;
    inset: 0;
  }
  .brand {
    position: absolute;
    left: 84px;
    top: 140px;
    width: 260px;
    text-align: center;
    color: var(--ink);
    font-weight: 400;
  }
  .brand-mark {
    width: 150px;
    height: 150px;
    margin: 0 auto 18px;
    border-radius: 50%;
    background: var(--brand-circle);
  }
  .brand-name {
    margin: 0;
    font-size: 34px;
    line-height: 1.05;
    letter-spacing: 0.5px;
  }
  .divider {
    position: absolute;
    left: 425px;
    top: 150px;
    width: 1.5px;
    height: 320px;
    background: var(--ink-soft);
  }
  .details {
    position: absolute;
    left: 442px;
    top: 205px;
    color: var(--ink);
  }
  .practitioner {
    margin: 0 0 70px;
    font-size: 21px;
    font-weight: 600;
  }
  .address {
    margin: 0 0 20px;
    font-style: normal;
    font-size: 17px;
    line-height: 1.45;
  }
  .contact {
    list-style: none;
    margin: 0;
    padding: 0;
    font-size: 16.5px;
    line-height: 1.4;
  }
  .contact li {
    display: flex;
    align-items: center;
    gap: 8px;
  }
  .contact svg {
    width: 13px;
    height: 13px;
    flex: none;
  }
</style>
</head>
<body>
<main class="canvas">
  <section class="card" aria-label="Quiet Fern Acupuncture appointment card">
    <svg class="card-shape" viewBox="0 0 880 500" aria-hidden="true">
      <defs>
        <linearGradient id="side-left" x1="0" y1="0" x2="1" y2="0">
          <stop offset="0" stop-color="var(--orange-deep)"/>
          <stop offset="1" stop-color="var(--orange-light)"/>
        </linearGradient>
        <linearGradient id="side-right" x1="1" y1="0" x2="0" y2="0">
          <stop offset="0" stop-color="var(--orange-deep)"/>
          <stop offset="1" stop-color="var(--orange-light)"/>
        </linearGradient>
      </defs>
      <rect x="0" y="0" width="440" height="500" fill="url(#side-left)"/>
      <rect x="440" y="0" width="440" height="500" fill="url(#side-right)"/>
      <path d="M90,0 L790,0 Q890,250 790,500 L90,500 Q-10,250 90,0 Z" fill="var(--edge-black)"/>
      <path d="M102,0 L778,0 Q870,250 778,500 L102,500 Q10,250 102,0 Z" fill="var(--card-white)"/>
    </svg>

    <div class="brand">
      <div class="brand-mark" aria-hidden="true"></div>
      <p class="brand-name">Quiet Fern<br>acupuncture</p>
    </div>

    <div class="divider" aria-hidden="true"></div>

    <div class="details">
      <p class="practitioner">Marla Pennick-Vasquez, LAc, Dipl, Ac</p>
      <address class="address">
        2730 N Ridley Avenue, Suite 410<br>
        Flagstaff, AZ, 86044<br>
        @ Haverstock Chiropractic
      </address>
      <ul class="contact">
        <li>
          <svg viewBox="0 0 16 16" aria-hidden="true"><path d="M4 1 L6.5 4.5 L5 6.2 C6 8.4 7.6 10 9.8 11 L11.5 9.5 L15 12 L13 15 C7 14.5 1.5 9 1 3 Z" fill="var(--accent)"/></svg>
          (928) 555-0142
        </li>
        <li>
          <svg viewBox="0 0 16 16" aria-hidden="true"><rect x="1" y="3" width="14" height="10" fill="none" stroke="var(--accent)" stroke-width="1.6"/><path d="M1 3 L8 9 L15 3" fill="none" stroke="var(--accent)" stroke-width="1.6"/></svg>
          quietfernacupuncture@mailbox-example.com
        </li>
      </ul>
    </div>
  </section>
</main>
</body>
</html>
```